Meal Prep Business in need of flyer

We are a company specializing in healthy meals and meals prep. We would like an eye catching flyer to post in town and in gyms. We would like the flyer to include Local(Labrador West) next day delivery. Shipping to Churchill Falls, Goose Bay and St. John's, NL. Customized meal plans.

I would like something that highlights our sponsored athletes as well Carla Venmore - National Figure Competitor and 2015 QMFDU Overall Figure Champ and Tess Morrow National Bikini Competitor and 2016 QMFDU Overall Bikini Champ.
I would like to have the WE-SHOP WE COOK WE DELIVER and our email colin@vitalforkkitchen.com.

The final design should communicate how we save you time while living a healthier or fitness orientated lifestyle and drive people to our website. Website is www.vitalforkkitchen.com

Target Market(s)

Fitness, meal prep, people looking to eat heathier, people looking to lose weight. and people looking to save time

Industry/Entity Type

Nutrition

Contact Information for Business Card

We are a company specializing in healthy meals and meals prep. We would like an eye catching business card . We would like the flyer to include Local(Labrador West) next day delivery.
Shipping to Churchill Falls,
Goose Bay and
St. John's, NL.

We do Customized meal plans.
i would like something that highlights our sponsored athletes as well Carla Venmore - National Figure Competitor and 2015 QMFDU Overall Figure Champ and Tess Morrow National Bikini Competitor and 2016 QMFDU Overall Classic Bikini Champ. I would like to have the WE-SHOP WE COOK WE DELIVER, phone number 7090341-0582 and our email colin@vitalforkkitchen.com.The final design should communicate living a healthier lifestyle and drive people to our website. Website is www.vitalforkkitche.com

Colors
3176b5
0255a3
33a6d7
0492cd

Requirements
Must have
• Flyer - Logo, Next day shipping, shipping to Goose Bay, Churchill Falls & St John's, NL. Sponsored athletes, website, slogan, customized meals plans, a couple of picture of our meals
• business card - logo, website, slogan, phone number, email, next day shipping, shipping to Goose Bay, Churchill Falls & St John's, NL,
Nice to have
• Flyer - Sponsored athletes pictures, flyer to be a template to change pics and any info
• Business card - sponsored athletes, picture of our meals

```html
<!DOCTYPE html>
<html lang="en">
<head>
<meta charset="utf-8">
<title>Vital Fork Kitchen – Flyer</title>
<link rel="stylesheet" href="https://fonts.googleapis.com/css2?family=Roboto+Condensed:wght@400;500;700&family=Roboto:wght@400;500&display=swap">
<style>
  :root{
    --blue-deep:#0255a3;
    --blue-mid:#3176b5;
    --blue-bright:#0492cd;
    --blue-sky:#33a6d7;
    --white:#ffffff;
    --page:#e6e8eb;
    --ink-soft:#1c5fa8;
  }
  *{margin:0;padding:0;box-sizing:border-box}
  html,body{width:900px;height:1200px;overflow:hidden;background:var(--page)}
  .flyer{
    position:absolute;left:40px;top:21px;
    width:596px;height:842px;
    transform:scale(1.376);transform-origin:0 0;
    background:var(--white);overflow:hidden;
    font-family:"Roboto Condensed",Arial,sans-serif;
    box-shadow:0 2px 6px rgba(0,0,0,.18);
  }
  .flyer-art{position:absolute;inset:0;width:596px;height:842px}

  .brand-badge{
    position:absolute;left:327px;top:278px;width:156px;height:156px;
    display:flex;flex-direction:column;align-items:center;justify-content:center;
    color:var(--blue-deep);font-weight:700;text-transform:uppercase;text-align:center;line-height:1;
  }
  .brand-badge .brand-name{font-size:27px;letter-spacing:.5px}
  .brand-badge .brand-sub{font-size:15px;letter-spacing:3px;margin-top:3px}

  .athlete{position:absolute;left:0;width:250px;text-align:center;color:var(--white)}
  .athlete-photo{
    display:block;margin:0 auto;width:150px;height:120px;border:3px solid var(--white);
  }
  .athlete-one .athlete-photo{background:linear-gradient(160deg,#a2344d 0%,#7d2a3f 55%,#c98f6d 100%)}
  .athlete-two .athlete-photo{background:linear-gradient(160deg,#3f6fc4 0%,#2a3f8f 50%,#6ca3d9 100%)}
  .athlete-name{font-size:12.5px;font-weight:700;margin-top:9px}
  .athlete-title{font-family:"Roboto",Arial,sans-serif;font-size:7.6px;line-height:1.35;margin-top:3px}
  .athlete-one{top:475px}
  .athlete-two{top:663px}
  .athlete-divider{position:absolute;left:18px;top:654px;width:212px;height:1px;background:rgba(255,255,255,.8)}

  .slogan{position:absolute;left:274px;top:456px;display:flex;align-items:center;color:var(--blue-deep);font-weight:700}
  .slogan-we{font-size:112px;line-height:1;letter-spacing:-4px}
  .slogan-verbs{list-style:none;font-size:31px;line-height:30px;margin-left:4px;text-transform:uppercase}

  .rule{position:absolute;left:278px;width:304px;height:1px;background:var(--blue-mid)}
  .rule-top{top:578px}
  .rule-bottom{top:758px}

  .services{position:absolute;left:287px;top:594px;color:var(--ink-soft)}
  .services-heading{font-size:27px;font-weight:700;color:var(--blue-deep);line-height:1}
  .services-list{list-style:none;margin-top:8px;font-size:13.5px;line-height:16px}
  .services-list li{position:relative;padding-left:15px;margin-bottom:9px}
  .services-list li svg{position:absolute;left:0;top:1px;width:11px;height:11px}

  .contact{position:absolute;left:275px;color:var(--blue-bright);display:flex;align-items:center;font-family:"Roboto",Arial,sans-serif}
  .contact svg{width:20px;height:20px;margin-right:9px;flex:none}
  .contact-email{top:777px;font-size:15px}
  .contact-web{top:803px;font-size:17.5px}
</style>
</head>
<body>
<div class="flyer">
  <svg class="flyer-art" viewBox="0 0 596 842" aria-hidden="false">
    <defs>
      <linearGradient id="pancakeTone" x1="0" y1="0" x2="0" y2="1">
        <stop offset="0" stop-color="#c98a45"/><stop offset=".5" stop-color="#a0612c"/><stop offset="1" stop-color="#7a4520"/>
      </linearGradient>
      <linearGradient id="trayTone" x1="0" y1="0" x2="1" y2="1">
        <stop offset="0" stop-color="#c9772f"/><stop offset=".5" stop-color="#3f6d2a"/><stop offset="1" stop-color="#d88a70"/>
      </linearGradient>
      <linearGradient id="saladTone" x1="0" y1="0" x2="0" y2="1">
        <stop offset="0" stop-color="#e8c4a8"/><stop offset=".5" stop-color="#e0a060"/><stop offset="1" stop-color="#f0ebe4"/>
      </linearGradient>
      <linearGradient id="sidebarBlue" x1="0" y1="0" x2="1" y2="1">
        <stop offset="0" stop-color="#0a5bb0"/><stop offset="1" stop-color="#2a9bd8"/>
      </linearGradient>
    </defs>

    <polygon role="img" aria-label="Photo of a stack of pancakes with butter and syrup" points="0,0 224,0 140,470 0,470" fill="url(#pancakeTone)"/>
    <polygon role="img" aria-label="Photo of a meal prep tray with sweet potato, broccoli and salmon" points="230,0 449,0 380,420 146,470" fill="url(#trayTone)"/>
    <polygon role="img" aria-label="Photo of meal prep containers with chicken and vegetable rice" points="455,0 596,0 596,420 386,420" fill="url(#saladTone)"/>

    <path d="M0,402 C110,470 260,472 360,448 C460,424 540,392 596,368 L596,842 L0,842 Z" fill="var(--white)"/>
    <path d="M0,402 C110,470 260,472 360,448 C460,424 540,392 596,368 L596,420 C530,440 460,456 370,462 C280,468 255,466 250,466 L250,842 L0,842 Z" fill="url(#sidebarBlue)"/>
    <path d="M0,418 C120,478 270,476 370,452 C470,430 545,400 596,384" fill="none" stroke="var(--white)" stroke-width="2"/>

    <circle cx="405" cy="356" r="77" fill="var(--white)" stroke="var(--blue-bright)" stroke-width="3"/>
  </svg>

  <div class="brand-badge">
    <span class="brand-name">Vital Fork</span>
    <span class="brand-sub">Kitchen</span>
  </div>

  <div class="athlete athlete-one">
    <div class="athlete-photo" role="img" aria-label="Photo of athlete Carla Venmore on stage"></div>
    <p class="athlete-name">Carla Venmore</p>
    <p class="athlete-title">National Figure Competitor and 2015 QMFDU<br>Overall Figure Champ</p>
  </div>
  <div class="athlete-divider"></div>
  <div class="athlete athlete-two">
    <div class="athlete-photo" role="img" aria-label="Photo of athlete Tess Morrow on stage"></div>
    <p class="athlete-name">Tess Morrow</p>
    <p class="athlete-title">National Bikini Competitor and 2016 QMFDU<br>Overall Bikini Champ.</p>
  </div>

  <div class="slogan">
    <span class="slogan-we">WE</span>
    <ul class="slogan-verbs"><li>Shop</li><li>Cook</li><li>Deliver</li></ul>
  </div>

  <div class="rule rule-top"></div>

  <section class="services">
    <h2 class="services-heading">Our services:</h2>
    <ul class="services-list">
      <li><svg viewBox="0 0 12 12"><path d="M1,6 L4.5,10 L11,1" fill="none" stroke="currentColor" stroke-width="1.6"/></svg>Local(Labrador West)<br>next day delivery</li>
      <li><svg viewBox="0 0 12 12"><path d="M1,6 L4.5,10 L11,1" fill="none" stroke="currentColor" stroke-width="1.6"/></svg>Shipping to Churchill Falls</li>
      <li><svg viewBox="0 0 12 12"><path d="M1,6 L4.5,10 L11,1" fill="none" stroke="currentColor" stroke-width="1.6"/></svg>Goose Bay and St. John’s</li>
      <li><svg viewBox="0 0 12 12"><path d="M1,6 L4.5,10 L11,1" fill="none" stroke="currentColor" stroke-width="1.6"/></svg>NL. Customized meal plans.</li>
    </ul>
  </section>

  <div class="rule rule-bottom"></div>

  <p class="contact contact-email">
    <svg viewBox="0 0 20 20"><circle cx="10" cy="10" r="9.5" fill="#222"/><rect x="5" y="6.5" width="10" height="7" fill="none" stroke="#fff" stroke-width="1"/><path d="M5,6.5 L10,10.5 L15,6.5" fill="none" stroke="#fff" stroke-width="1"/></svg>
    colin@vitalforkkitchen.com.
  </p>
  <p class="contact contact-web">
    <svg viewBox="0 0 20 20"><circle cx="10" cy="10" r="9.5" fill="#222"/><circle cx="10" cy="10" r="6" fill="none" stroke="#fff" stroke-width="1"/><ellipse cx="10" cy="10" rx="2.6" ry="6" fill="none" stroke="#fff" stroke-width="1"/><path d="M4,10 H16 M5,7 H15 M5,13 H15" stroke="#fff" stroke-width=".8"/></svg>
    www.vitalforkkitchen.com
  </p>
</div>
</body>
</html>
```